VelloPath Business Card

Our company is called VelloPath and we are based in Tel Aviv, Israel. We create innovative and exciting methods for getting people on the web engaged with content. We need a cool yet professional business card that will represent our management level employees. keep in mind this is a start up company with a young atmosphere. You can be inspired by our logo (file attached, make sure you have the right font "Ubuntu-Condensed") Use the colors that are used in the logo and create a colourful and professional business card.

```html
<!DOCTYPE html>
<html lang="en">
<head>
<meta charset="utf-8">
<title>VelloPath Business Card</title>
<link href="https://fonts.googleapis.com/css2?family=Ubuntu+Condensed&family=Ubuntu:wght@400;500;700&display=swap" rel="stylesheet">
<style>
  :root {
    --stage: #e9e6e1;
    --paper: #ffffff;
    --ink: #3a3a3a;
    --muted: #6f6f6f;
    --night: #151617;
    --night-edge: #26292c;
    --magenta: #e0309a;
    --purple: #a64dc0;
    --cyan: #5cc3e8;
    --blue: #2a9fd8;
    --lime: #a9d45a;
    --yellow: #f7dd3a;
    --orange: #f8b94c;
  }
  * { margin: 0; padding: 0; box-sizing: border-box; }
  html, body { width: 1200px; height: 1023px; overflow: hidden; }
  body {
    background: var(--stage);
    position: relative;
    font-family: "Ubuntu", sans-serif;
  }
  .card {
    position: absolute;
    width: 560px;
    height: 340px;
    border-radius: 6px;
    overflow: hidden;
    box-shadow: 0 14px 30px rgba(0,0,0,0.18);
  }
  /* Front */
  .card-front { left: 60px; top: 110px; background: var(--paper); }
  .bubble-field {
    position: absolute;
    top: 0; right: 0;
    width: 400px; height: 210px;
    background:
      radial-gradient(circle at 25% 75%, rgba(247,221,58,0.55), transparent 45%),
      radial-gradient(circle at 70% 30%, rgba(224,48,154,0.45), transparent 45%),
      radial-gradient(circle at 90% 80%, rgba(169,212,90,0.5), transparent 40%),
      radial-gradient(circle at 45% 20%, rgba(92,195,232,0.5), transparent 45%),
      linear-gradient(135deg, rgba(248,185,76,0.25), rgba(166,77,192,0.25));
    border-bottom-left-radius: 120px;
  }
  .identity { position: absolute; left: 250px; top: 150px; }
  .identity .name {
    font-weight: 700;
    font-size: 22px;
    letter-spacing: 1px;
    color: var(--purple);
    text-transform: uppercase;
  }
  .identity .role {
    margin-top: 4px;
    font-size: 12px;
    letter-spacing: 1.5px;
    color: var(--muted);
    text-transform: uppercase;
  }
  .brand {
    position: absolute;
    display: flex;
    align-items: center;
    gap: 10px;
    font-family: "Ubuntu Condensed", sans-serif;
    font-weight: 400;
  }
  .brand .dot { border-radius: 50%; }
  .card-front .brand { left: 30px; top: 200px; font-size: 34px; color: var(--ink); }
  .card-front .brand .dot { width: 22px; height: 22px; background: var(--magenta); }
  .contacts {
    position: absolute;
    right: 30px; top: 212px;
    list-style: none;
    font-size: 12.5px;
    color: var(--muted);
  }
  .contacts li { display: flex; align-items: center; gap: 8px; margin-bottom: 6px; }
  .contacts svg { width: 15px; height: 15px; flex: none; }
  .address-strip {
    position: absolute;
    left: 0; right: 0; bottom: 0;
    height: 36px;
    background: var(--night-edge);
    color: var(--cyan);
    font-weight: 500;
    font-size: 13px;
    letter-spacing: 1px;
    text-transform: uppercase;
    display: flex; align-items: center; justify-content: center;
  }
  /* Back */
  .card-back {
    left: 580px; top: 570px;
    background: linear-gradient(160deg, #2a2c2f 0%, var(--night) 55%, #0c0c0d 100%);
  }
  .card-back .brand {
    left: 50%; top: 50%;
    transform: translate(-50%, -50%);
    font-size: 50px;
    color: #ffffff;
  }
  .card-back .brand .dot { width: 30px; height: 30px; background: var(--cyan); }
</style>
</head>
<body>
  <section class="card card-front" aria-label="Business card front">
    <div class="bubble-field" role="img" aria-label="Scattered coloured bubble pattern in pink, yellow, cyan, lime and orange"></div>
    <div class="identity">
      <p class="name">Dana Levinor</p>
      <p class="role">Founder | CEO</p>
    </div>
    <div class="brand"><span class="dot"></span><span>VelloPath</span></div>
    <ul class="contacts">
      <li>
        <svg viewBox="0 0 16 16"><circle cx="8" cy="8" r="8" fill="var(--lime)"/><path d="M5.2 4.5l1.4-.3.8 1.9-.9.7c.5 1 1.2 1.7 2.2 2.2l.7-.9 1.9.8-.3 1.4c-3.2.2-6-2.6-5.8-5.8z" fill="#fff"/></svg>
        <span>+972 3 555 0142</span>
      </li>
      <li>
        <svg viewBox="0 0 16 16"><circle cx="8" cy="8" r="8" fill="var(--magenta)"/><rect x="4" y="5" width="8" height="6" rx="0.8" fill="#fff"/><path d="M4.3 5.4L8 8.3l3.7-2.9" stroke="var(--magenta)" stroke-width="0.9" fill="none"/></svg>
        <span>dana@vellopath.com</span>
      </li>
      <li>
        <svg viewBox="0 0 16 16"><circle cx="8" cy="8" r="8" fill="var(--purple)"/><g stroke="#fff" stroke-width="0.9" fill="none"><circle cx="8" cy="8" r="4"/><ellipse cx="8" cy="8" rx="1.8" ry="4"/><path d="M4 8h8"/></g></svg>
        <span>www.vellopath.com</span>
      </li>
    </ul>
    <div class="address-strip">Harbour Lane 14, 6100 Tel Aviv, Israel</div>
  </section>

  <section class="card card-back" aria-label="Business card back">
    <div class="brand"><span class="dot"></span><span>VelloPath</span></div>
  </section>
</body>
</html>
```